Swimming Pool Service Website needed!!!

Hi Everyone! Thanks for looking at my contest. I PROMISE to provide excellent feedback during this process.

I am starting a new swimming pool business cleaning company in San Diego, California and would like your help in making it similar to one of these two websites that are already functioning.

http://www.brightlagoonworks.example/services-repair.html

http://tidemarkaquacare.example/commercial-pool-cleaning.php

I like these two because they are easy to read, classy, sophisticated and have nice pictures of really clean & clear pools.

I really like the blue on white color format.

I do not have a logo, but the name of my company is GLIMMERWAVE POOL SERVICE.

My tag line is: Water so pure, it sparkles like a summer sky. (does not need to have the quotes around "in"...maybe just italics for this word IN?) You decide for me.

I would like to have a logo designed that incorporates some sort of easy to read letters. I do not want cursive (handwriting) letters. I thought about having a "reflection" of letters (mirror image), but think that this will be hard to read from far away. Maybe you can surprise me and come up with an idea that works using the a mirror image....but I'm not sure. I was leaning toward plain old BLOCK letters as I think it would be easy to read on my truck.

I would like to have 5 pages on my website:
1) Home
2) About Us (Know Your Poolman) / Why Hire Us
3) Services Offered
4) FAQ's
5) Contact

I am looking for a fully-functioning website (coded). Upon selection of the design winner, I am offering to increase the budget/payment by $100-$125 for the coding of all the pages. So anyone looking at participating in this contest, should be willing and able to provide the coding to the webpages that i've requested.

Target Market(s)

Upper middle-class homeowners who have a pool

Industry/Entity Type

Pool Service

Number of Pages Required

5+ page

Font styles to use
Serif

Colors
0455a3
3276b5
85acd3
85cae6
ffffff
33a6d7
0592cd

Requirements
Must have
• The Home page must have this picture highlighted in the top of the page:
• http://www.mesawaterpro.example/
• Must have pictures of some high-end pools. Any that you can find on the internet are wonderful.
• Must have a table on the right of the home page that mentions the service areas that we go to:
• • Carmel Valley (92130)
• • Del Mar (92014)
• • Rancho Santa Fe (92067)
• • Solana Beach (92075)
• • Santaluz (92127)
• • Cardiff (92007)
• • Encinitas (92024)
• • Carlsbad (92009, 92008)
• • La Jolla (92037)
• • Pacific Beach (92109)
• • Mira Mesa (92126)
• • Sorrento Valley (92121)
• • Clairemont (92117)
• • Rancho Bernardo (92127, 92128)
• • Rancho Penasquitos (92129)
• • Poway (92064)
• •
Nice to have
• Maybe incorporate some pictures of some kids (or families) playing in pools on the Why Hire Us page?
• I also like the feel of this website, but posting this page just for reference so you can get a feel more of what I like:
• http://www.crestlinepool.example/
• I like the FAQ's page from this website. I like how you can click on the question and then it pops up with the answer. http://www.dunewoodpoolcare.example/pool-spa-fountain-faqs/

```html
<!DOCTYPE html>
<html lang="en">
<head>
<meta charset="utf-8">
<title>GlimmerWave Pool Service</title>
<link rel="stylesheet" href="https://fonts.googleapis.com/css2?family=Open+Sans:ital,wght@0,400;0,600;0,700;1,400&family=Lora:ital,wght@1,400;1,600&display=swap">
<style>
:root{
  --navy:#0455a3;
  --blue:#3276b5;
  --sky:#85acd3;
  --aqua:#85cae6;
  --cyan:#33a6d7;
  --ocean:#0592cd;
  --white:#ffffff;
  --ink:#4a5560;
  --line:#d6e2ee;
}
*{box-sizing:border-box;margin:0;padding:0}
html,body{width:720px;height:1200px;overflow:hidden;background:var(--white)}
body{font-family:"Open Sans",Arial,sans-serif;color:var(--ink);position:relative}
.page{position:absolute;left:90px;top:0;width:540px}

.site-header{position:relative;height:84px}
.brand{position:absolute;left:0;top:20px;display:flex;align-items:center;gap:7px}
.brand-dot{width:22px;height:22px;border-radius:50%;background:var(--navy)}
.brand-name{font-family:"Open Sans",Arial,sans-serif;font-weight:700;color:var(--navy);font-size:13px;line-height:14px;letter-spacing:.5px}
.tagline{position:absolute;right:0;top:30px;font-family:"Lora",Georgia,serif;font-style:italic;color:var(--ocean);font-size:12.5px}
.tagline em{font-weight:600}
.main-nav{position:absolute;left:0;right:0;top:62px;height:18px;border-bottom:1px solid var(--line);display:flex;justify-content:flex-end;gap:20px;font-size:7.5px;color:var(--blue);text-transform:uppercase;letter-spacing:.3px}
.main-nav a{color:inherit;text-decoration:none}

.hero{position:absolute;left:0;top:88px;width:540px;height:244px;background:linear-gradient(180deg,#7fc2ec 0%,#b9e2f6 34%,#3aa9dc 52%,#0a86c6 100%)}
.hero-callout{position:absolute;right:14px;top:28px;width:182px}
.hero-lead{background:rgba(4,85,163,.55);color:var(--white);font-weight:700;font-size:11.5px;line-height:14px;padding:7px 9px}
.hero-lead small{display:block;font-weight:400;font-size:7.5px;margin-top:3px}
.hero-call{margin-top:4px;background:rgba(3,50,96,.85);color:var(--white);font-size:8px;line-height:11px;font-weight:600;padding:5px 9px}

.col-left{position:absolute;left:0;top:378px;width:250px}
.col-mid{position:absolute;left:262px;top:378px;width:128px}
.col-right{position:absolute;left:402px;top:378px;width:138px}

.section-bar{display:flex;align-items:center;gap:6px;height:20px;background:var(--navy);color:var(--white);font-size:9px;font-weight:700;padding:0 7px;margin-bottom:8px}
.section-bar svg{flex:none}
p{font-size:6.6px;line-height:9.6px;margin-bottom:7px}
.col-left .mission{margin-top:18px}

.kid-photo{width:128px;height:92px;background:linear-gradient(160deg,#9ad6ef,#2f9fd4);margin-bottom:9px}

.areas{list-style:none;font-size:6.6px;line-height:9.4px;margin-bottom:10px}
.areas li::before{content:"• ";color:var(--ocean)}
.guarantee{background:var(--ocean);color:var(--white);padding:9px 8px 4px;font-weight:600}
.guarantee p{font-size:6.8px;line-height:9.8px}

.site-footer{position:absolute;left:0;top:834px;width:540px;height:18px;background:var(--sky);color:var(--white);font-size:6.5px;display:flex;align-items:center;justify-content:center;gap:10px}
</style>
</head>
<body>
<div class="page">
  <header class="site-header">
    <div class="brand">
      <span class="brand-dot"></span>
      <span class="brand-name">GLIMMERWAVE<br>POOL SERVICE</span>
    </div>
    <div class="tagline">"Water so pure, it sparkles like a summer sky."</div>
    <nav class="main-nav">
      <a href="#">Home</a><a href="#">About Us</a><a href="#">Services Offered</a><a href="#">FAQs</a><a href="#">Contact</a>
    </nav>
  </header>

  <section class="hero" role="img" aria-label="Photo of a high-end swimming pool with clear blue water under a bright sky">
    <div class="hero-callout">
      <div class="hero-lead">Leading San Diego swimming pool and spa service company<small>| Both commercial and residential |</small></div>
      <div class="hero-call">Call us today to schedule a FREE pool and needs assessment (858) 555-0147</div>
    </div>
  </section>

  <div class="col-left">
    <div class="section-bar">
      <svg width="12" height="12" viewBox="0 0 12 12"><circle cx="6" cy="6" r="6" fill="#fff"/><path d="M2 7c1.3-1 2.7-1 4 0s2.7 1 4 0" stroke="#0455a3" fill="none" stroke-width="1.2"/></svg>
      Commercial and Residential Pool Service
    </div>
    <p>If you're looking for the best pool cleaning service at an affordable price available in San Diego, we would love the opportunity to prove GlimmerWave Pool Service is the answer. We are a family-owned company that has built its name on trust, reliable weekly visits and water that stays crystal clear through every season of the year.</p>
    <p>Customer satisfaction is our highest priority, and we ensure every visit leaves your pool clean, balanced and ready for a swim.</p>

    <div class="section-bar mission">
      <svg width="12" height="12" viewBox="0 0 12 12"><circle cx="6" cy="6" r="6" fill="#fff"/><path d="M3.2 6.2l2 2 3.6-4" stroke="#0455a3" fill="none" stroke-width="1.3"/></svg>
      Our Mission
    </div>
    <p>At GlimmerWave Pool Service, we understand that your pool is an important investment. Whether you use it for family fun or quiet relaxation, it needs to be well cared for. Our technicians bring years of experience, careful attention to detail and a genuine pride in keeping your water safe, healthy and inviting.</p>
    <p>We treat every customer like a neighbor. Our goal is simple: dependable service, honest pricing and a sparkling pool you can enjoy every single day.</p>
  </div>

  <div class="col-mid">
    <div class="kid-photo" role="img" aria-label="Photo of a child relaxing on a float in a bright blue pool"></div>
    <p>We offer both residential and commercial pool cleaning, service and maintenance throughout North County and coastal San Diego.</p>
    <p>Our certified technicians test and balance chemicals, brush walls and tile, empty baskets and inspect equipment on every visit.</p>
    <p>Make sure your pool is ready for the summer season. Call today for a free estimate.</p>
  </div>

  <aside class="col-right">
    <div class="section-bar">
      <svg width="10" height="12" viewBox="0 0 10 12"><path d="M5 0a4 4 0 0 0-4 4c0 3 4 8 4 8s4-5 4-8a4 4 0 0 0-4-4z" fill="#fff"/><circle cx="5" cy="4" r="1.5" fill="#0455a3"/></svg>
      Service Areas
    </div>
    <p>We are proud to provide our weekly pool service to the following San Diego County areas:</p>
    <ul class="areas">
      <li>Carmel Valley (92130)</li>
      <li>Del Mar (92014)</li>
      <li>Rancho Santa Fe (92067)</li>
      <li>Solana Beach (92075)</li>
      <li>Santaluz (92127)</li>
      <li>Cardiff (92007)</li>
      <li>Encinitas (92024)</li>
      <li>Carlsbad (92009, 92008)</li>
      <li>La Jolla (92037)</li>
      <li>Pacific Beach (92109)</li>
      <li>Mira Mesa (92126)</li>
      <li>Sorrento Valley (92121)</li>
      <li>Clairemont (92117)</li>
      <li>Rancho Bernardo (92127, 92128)</li>
      <li>Rancho Penasquitos (92129)</li>
      <li>Poway (92064)</li>
    </ul>
    <div class="guarantee">
      <p>We guarantee your satisfaction on each and every service call and repair. Your pool, spa or fountain should be a relaxing and safe retreat for your family.</p>
      <p>If you are not happy with your visit, let us know and we will return at no extra charge.</p>
    </div>
  </aside>

  <footer class="site-footer">
    <span>© 2013 GlimmerWave Pool Service. Proudly serving San Diego.</span>
    <span>Contact | Privacy</span>
  </footer>
</div>
</body>
</html>
```